C U B A N - C I G A R S - F L Y E R

I need a double-sided 5x7 club type flyer for a Memorial Day Weekend Trip.
The main side design needs to be similar to the attached flyer example. The front design of flyer is KEY. The design will be awarded to the closest finished submission to the example flyer.
Both sides of the flyer should also included event and business logo, which are also attached. Both logos can be altered to fit printing need accordingly.
Front side content is also attached.
The back side design will be very simple. Consists of 3 travel images and trip description, and my contact very details. Same color design as front. The attached word document contains backside details for REFERENCE ONLY. Please focus on front side when submitting a design for this project.
Target Market(s)
A F R I C A N - A M E R I C A N - C I G A R - S M O K E R S
Industry/Entity Type
Travel Industry
Requirements
Must have
- All the elements of the attached information
Nice to have
- Masculine Images
Should not have
- Large Cigar focus to catch customer's attention

```html
<!DOCTYPE html>
<html lang="en">
<head>
<meta charset="utf-8">
<title>Cuba Cigar Gentlemen's Memorial Day Weekend Flyer</title>
<link rel="stylesheet" href="https://fonts.googleapis.com/css2?family=Oswald:wght@300;400;500;600;700&family=Lato:wght@400;700&family=EB+Garamond:ital@1&display=swap">
<style>
  :root{
    --page:#e9e5df;
    --ink:#1b1b1b;
    --gold:#d5aa0f;
    --navy:#1f3a8a;
    --red:#c8102e;
    --rail:#e4e4e4;
    --night:#120d0a;
    --white:#ffffff;
  }
  *{box-sizing:border-box;margin:0;padding:0}
  html,body{width:1200px;height:1200px;overflow:hidden;background:var(--page)}
  body{position:relative;font-family:'Lato',sans-serif;color:var(--ink)}

  /* ---------- Front side ---------- */
  .flyer-front{position:absolute;left:211px;top:16px;width:778px;height:562px;background:var(--night);overflow:hidden;box-shadow:0 4px 14px rgba(0,0,0,.25)}
  .hero-photo{position:absolute;left:0;top:0;width:464px;height:562px;
    background:radial-gradient(ellipse at 38% 62%, #8a5a22 0%, #4a2c12 28%, #1c120b 60%, #0b0806 100%)}
  .hero-photo-right{position:absolute;left:740px;top:0;width:38px;height:562px;background:linear-gradient(180deg,#2a1e16,#0d0907)}
  .inset-photo{position:absolute;left:266px;top:392px;width:196px;height:170px;
    background:linear-gradient(160deg,#5a3418 0%,#8b4a22 45%,#3a1d0e 100%)}
  .brand-mark{position:absolute;left:28px;top:400px;width:136px;height:136px;border:2px solid rgba(255,255,255,.9);border-radius:50%;
    display:flex;align-items:center;justify-content:center;text-align:center}
  .brand-mark span{font-family:'Lato',sans-serif;font-weight:700;color:var(--white);font-size:15px;line-height:1.25;letter-spacing:.08em;text-transform:uppercase}

  .rail{position:absolute;top:0;height:562px;width:20px;background:var(--rail)}
  .rail-left{left:464px}
  .rail-right{left:720px}
  .event-panel{position:absolute;left:484px;top:0;width:236px;height:562px;background:var(--gold);text-align:center}
  .ornament{position:absolute;left:84px;top:38px;width:68px;height:14px;border-radius:7px;background:var(--night)}
  .event-badge{position:absolute;left:10px;top:66px;width:216px;height:216px;border-radius:50%;border:3px solid var(--navy);
    display:flex;align-items:center;justify-content:center;padding:20px}
  .event-badge span{font-family:'Oswald',sans-serif;font-weight:600;color:var(--navy);font-size:24px;line-height:1.15;text-transform:uppercase}
  .tagline{position:absolute;left:0;width:236px;font-family:'Oswald',sans-serif;color:var(--navy);line-height:1}
  .tagline-1{top:304px;font-size:31px;font-weight:400}
  .tagline-2{top:340px;font-size:28px;font-weight:700}
  .tagline-3{top:374px;font-size:17px;font-weight:600}
  .pitch{position:absolute;left:0;top:410px;width:236px;font-family:'Oswald',sans-serif;font-weight:300;color:var(--ink);font-size:24px;line-height:26px}
  .pitch strong{display:block;font-weight:700;color:var(--navy);font-size:28px;line-height:30px}
  .date-band{position:absolute;left:-14px;top:500px;width:264px;height:34px;background:var(--white);
    font-family:'EB Garamond',serif;font-style:italic;color:var(--red);font-size:24px;line-height:34px}

  /* ---------- Back side ---------- */
  .flyer-back{position:absolute;left:211px;top:622px;width:778px;height:560px;background:var(--white);overflow:hidden;box-shadow:0 4px 14px rgba(0,0,0,.2)}
  .photo-row{position:absolute;left:26px;top:19px;width:726px;height:160px}
  .photo-tile{position:absolute;top:0;height:160px}
  .tile-cars{left:0;width:222px;background:linear-gradient(135deg,#c9c3b8 0%,#f0c400 40%,#1e6fd9 75%,#0c3f8c 100%)}
  .tile-map{left:231px;width:230px;background:linear-gradient(180deg,#eaf1fb 0%,#c9dcf3 70%,#f6a623 100%)}
  .tile-cigars{left:472px;width:254px;background:linear-gradient(160deg,#a0623a 0%,#7a4322 50%,#4a2a16 100%)}
  .story{position:absolute;left:26px;top:191px;width:726px;font-size:11.6px;line-height:15.2px;text-align:justify;color:var(--ink)}

  .facts{position:absolute;list-style:none;font-size:13px;line-height:21px}
  .facts li{position:relative;padding-left:8px}
  .facts li::before{content:"";position:absolute;left:0;top:9px;width:4px;height:4px;border-radius:50%;background:var(--navy)}
  .facts .note{padding-left:8px;font-weight:700}
  .facts .note::before{display:none}
  .facts .hl{color:var(--red)}
  .cost-list{left:26px;top:394px}

  .included{position:absolute;left:272px;top:346px;width:240px}
  .included h3,.deposit h3{font-family:'Oswald',sans-serif;font-weight:500;color:var(--red);font-size:19px;line-height:24px}
  .included ul{list-style:none;margin-top:3px;font-size:13px;line-height:16px}
  .included li{position:relative;padding-left:10px;margin-bottom:5px;text-align:justify}
  .included li::before{content:"";position:absolute;left:0;top:5px;width:4px;height:4px;border-radius:50%;background:var(--navy)}

  .deposit{position:absolute;left:526px;top:358px;width:236px;font-size:13.5px;line-height:20px}
  .deposit b{font-weight:700}
  .contact-lead{margin-top:12px}
  .contact-line{display:flex;align-items:center;gap:5px;color:var(--red);white-space:nowrap}
  .phone{font-family:'Oswald',sans-serif;font-weight:400;font-size:24px;line-height:30px;letter-spacing:.02em}
  .web{font-weight:700;font-size:11px;letter-spacing:0}
  .contact-line svg{flex:none}
</style>
</head>
<body>

<section class="flyer-front" aria-label="Flyer front">
  <div class="hero-photo" role="img" aria-label="Photo of a glass of rum, a straw fedora and a lit cigar on a dark table"></div>
  <div class="hero-photo-right" role="img" aria-label="Continuation of the dark table photo"></div>
  <div class="inset-photo" role="img" aria-label="Photo of a man and a woman relaxing in a cigar lounge bar"></div>
  <div class="brand-mark"><span>Coastline<br>Voyages</span></div>

  <div class="rail rail-left"></div>
  <div class="event-panel">
    <div class="ornament" role="img" aria-label="Decorative flourish"></div>
    <div class="event-badge"><span>Memorial Day Weekend Cuba Trip May 25–28</span></div>
    <p class="tagline tagline-1">A CUBA CIGAR</p>
    <p class="tagline tagline-2">GENTLEMEN’S</p>
    <p class="tagline tagline-3">MEMORIAL DAYWEEKEND</p>
    <p class="pitch">Legally travel to Cuba<br>and return with real<strong>CUBAN CIGARS!</strong></p>
    <p class="date-band">25.05 - Tuesday 29.05</p>
  </div>
  <div class="rail rail-right"></div>
</section>

<section class="flyer-back" aria-label="Flyer back">
  <div class="photo-row">
    <div class="photo-tile tile-cars" role="img" aria-label="Photo of colourful classic American cars parked in Havana"></div>
    <div class="photo-tile tile-map" role="img" aria-label="Map showing the flight route from Miami to Havana, Cuba"></div>
    <div class="photo-tile tile-cigars" role="img" aria-label="Close-up photo of a row of Cuban cigars"></div>
  </div>

  <p class="story">Cuba is the ultimate bucket list destination for any cigar lover. Now is your opportunity to legally travel to Cuba and experience a country that has been off limits to Americans for more than 50 years before it changes. Smoke fine Cuban cigars, meet its resilient people and experience Cuba’s fascinating culture. Tour cigar factories, watch expert cigar rollers, visit a humidor factory and work-shop, tour the Old Harbor Rum Museum to learn firsthand the process of making rum followed by rum tasting and pairings with Cuban cigars in a private setting and much more. Explore the Pinar Del Rio located in the Viñales Valley known for its stunning land-scapes and tobacco plantations. Visit the world famous Valle Verde Tobacco Plantation to see first hand where and how the tobacco process is grown for fine Cuban Cigars. The bucket list trip of a lifetime awaits on this ‘people to people’ Cigar Journey to Cuba to learn first hand about Cuban cigars, meet the Cuban people, experience incredible cuisine, drive in classic American cars along the Malecon and experience the Cuban cigar process from ‘seed to smoke’ and an opportunity to smoke in the birthplace of cigars!</p>

  <ul class="facts cost-list">
    <li>Trip Cost: <span class="hl">$2050</span></li>
    <li>Deposit: <span class="hl">$300</span></li>
    <li>Payment plans available</li>
    <li><span class="hl">$300</span> Deposit Required</li>
    <li>Final payment Due By <span class="hl">April 10, 2018</span></li>
    <li class="note">*NON-REFUNDABLE</li>
    <li class="note">*Passport Required</li>
  </ul>

  <div class="included">
    <h3>What’s Included:</h3>
    <ul>
      <li>4 Days / 3 Nights</li>
      <li>5 Star Hotel Accommodations Based on Double Occupancy</li>
      <li>Roundtrip Palmline Airline Tickets from Fort Lauderdale Florida - Cuba</li>
      <li>Tour Bus Chauffeured Transportation</li>
      <li>All Rum and Cigar Tour Events</li>
      <li>Select Meals (Breakfast, Welcome and Farewell Dinner) and More!</li>
    </ul>
  </div>

  <div class="deposit">
    <h3>$300 Deposit Required</h3>
    <p>Final payment Due By <b>April 10, 2018</b></p>
    <p><b>*NON-REFUNDABLE</b></p>
    <p><b>*Passport Required</b></p>
    <p class="contact-lead">For More Information Call</p>
    <p class="contact-line">
      <svg width="14" height="14" viewBox="0 0 24 24" aria-hidden="true"><circle cx="12" cy="12" r="10.5" fill="none" stroke="#1f3a8a" stroke-width="2"/><path d="M8 6.5l2 2-1.2 1.6c.8 1.8 2.2 3.2 4 4l1.6-1.2 2 2-1.4 1.9c-4-.6-7.9-4.5-8.5-8.5z" fill="#1f3a8a"/></svg>
      <span class="phone">XXX-XXX-XXXX</span>
    </p>
    <p>Book Today at:</p>
    <p class="contact-line">
      <svg width="11" height="11" viewBox="0 0 24 24" aria-hidden="true"><circle cx="12" cy="12" r="10" fill="none" stroke="#1f3a8a" stroke-width="2"/><ellipse cx="12" cy="12" rx="4.5" ry="10" fill="none" stroke="#1f3a8a" stroke-width="2"/><line x1="2" y1="12" x2="22" y2="12" stroke="#1f3a8a" stroke-width="2"/></svg>
      <span class="web">WWW.COASTLINEVOYAGES.com/CUBA2018</span>
    </p>
  </div>
</section>

</body>
</html>
```